Valdren Insight Powerpoint

Take an outdated PowerPoint and modernize it to our company's brand via google PowerPoint. Please check out our website at www.valdrengroup-example.com to see more styles but give it that intelligence twist. The powerpoint to work on is the Intelligence PP. Please keep it professional.

Target Market(s)

Security Industry / Silicon Valley

Industry/Entity Type

Executive Protection / Intelligence

Requirements
Must have
• Valdren Logo / Valdren Colors / Confidential notice at bottom
Nice to have
• Pictures of major cities / San Francisco
Should not have
• Pictures of anybody with ear pieces.

```html
<!DOCTYPE html>
<html lang="en">
<head>
<meta charset="utf-8">
<title>Valdren Insight – The Threat Environment</title>
<link href="https://fonts.googleapis.com/css2?family=Orbitron:wght@700;900&family=Mulish:wght@400;500;600&display=swap" rel="stylesheet">
<style>
  :root {
    --brand-red: #8b181d;
    --ink: #3a3a3c;
    --muted: #8a8a8d;
    --rule: #dcdcdc;
    --paper: #ffffff;
    --haze: #e9e9eb;
  }
  * { margin: 0; padding: 0; box-sizing: border-box; }
  html, body { width: 1200px; height: 675px; overflow: hidden; background: var(--paper); }
  .slide {
    position: relative;
    width: 1200px;
    height: 675px;
    background: var(--paper);
    font-family: "Mulish", sans-serif;
    color: var(--ink);
  }
  .network-backdrop {
    position: absolute;
    left: 0; top: 0;
    width: 1200px; height: 420px;
    background:
      radial-gradient(ellipse 420px 220px at 78% 22%, var(--haze) 0%, rgba(255,255,255,0) 100%),
      radial-gradient(ellipse 360px 200px at 40% 12%, #efeff0 0%, rgba(255,255,255,0) 100%),
      radial-gradient(ellipse 200px 300px at 4% 45%, #f0f0f1 0%, rgba(255,255,255,0) 100%);
  }
  .slide-title {
    position: absolute;
    left: 82px; top: 58px;
    font-family: "Orbitron", sans-serif;
    font-weight: 900;
    font-size: 24px;
    letter-spacing: 1.6px;
    word-spacing: 8px;
    color: var(--brand-red);
  }
  .intro {
    position: absolute;
    left: 82px; top: 137px;
    width: 200px;
    font-size: 15px;
    line-height: 21.5px;
    letter-spacing: 0.2px;
  }
  .intro p + p { margin-top: 7px; }
  .divider {
    position: absolute;
    left: 297px; top: 137px;
    width: 1px; height: 506px;
    background: var(--rule);
  }
  .methods-heading {
    position: absolute;
    left: 315px; top: 140px;
    font-size: 16px;
    font-weight: 600;
    letter-spacing: 0.1px;
  }
  .method {
    position: absolute;
    left: 315px;
    width: 830px;
    height: 74px;
    display: flex;
    align-items: center;
  }
  .method-tag {
    flex: 0 0 159px;
    height: 74px;
    background: var(--brand-red);
    color: #fff;
    display: flex;
    align-items: center;
  }
  .method-number {
    width: 53px;
    text-align: center;
    font-family: "Orbitron", sans-serif;
    font-weight: 900;
    font-size: 30px;
  }
  .method-label {
    font-size: 14.5px;
    line-height: 18px;
    font-weight: 500;
    letter-spacing: 0.3px;
  }
  .method-text {
    margin-left: 17px;
    width: 635px;
    font-size: 13.2px;
    line-height: 18.3px;
    letter-spacing: 0.1px;
  }
  .row-rule {
    position: absolute;
    left: 338px; width: 801px;
    height: 1px; background: var(--rule);
  }
  .brand-mark {
    position: absolute;
    left: 1040px; top: 621px;
    display: flex; align-items: center; gap: 7px;
    font-family: "Mulish", sans-serif;
    font-weight: 600;
    font-size: 18px;
    letter-spacing: 1px;
    color: var(--brand-red);
  }
  .brand-mark .brand-square { width: 14px; height: 14px; background: var(--brand-red); }
  .confidential-notice {
    position: absolute;
    left: 0; width: 1200px; top: 653px;
    text-align: center;
    font-size: 9px;
    letter-spacing: 1.5px;
    color: var(--muted);
  }
</style>
</head>
<body>
<div class="slide">
  <div class="network-backdrop" role="img" aria-label="Faint grey network of connected nodes across the top of the slide"></div>

  <h1 class="slide-title">THE THREAT ENVIRONMENT</h1>

  <div class="intro">
    <p>Executives have become easy targets for threat actors evident from a significant increase in both criminal and nation-state operations that are zeroing in on executives as the initial point of attack.</p>
    <p>Attackers lever publicly available information to learn about their target of choice and discover vulnerabilities to plan and carry out an attack. Reasons for these attack vary depending on motivating factors such financial reward, ideological, espionage or even physical harm.</p>
  </div>

  <div class="divider"></div>

  <h2 class="methods-heading">Here are just five methods among many that threat actors use to target executives.</h2>

  <div class="method" style="top:177px;">
    <div class="method-tag"><span class="method-number">1</span><span class="method-label">Data broker<br>profiles</span></div>
    <p class="method-text">Data broker profiles are risky for executives because they contain privileged information which hackers can leverage. Such as home IP addresses, passwords and financial information stored in the Dark Web and and confidential information about their family, relatives, and neighbors.</p>
  </div>
  <div class="row-rule" style="top:262px;"></div>

  <div class="method" style="top:272px;">
    <div class="method-tag"><span class="method-number">2</span><span class="method-label">Home<br>network and<br>devices</span></div>
    <p class="method-text">An executive’s home network and connected devices are a perfect target for hackers because it is usually not set up securely and as a result becomes a vector to exploit.</p>
  </div>
  <div class="row-rule" style="top:357px;"></div>

  <div class="method" style="top:367px;">
    <div class="method-tag"><span class="method-number">3</span><span class="method-label">Personal<br>accounts</span></div>
    <p class="method-text">One compromised Mailora or Linkora account can quickly snowball into several hijacked accounts, potentially leading to a full corporate breach.</p>
  </div>
  <div class="row-rule" style="top:452px;"></div>

  <div class="method" style="top:462px;">
    <div class="method-tag"><span class="method-number">4</span><span class="method-label">Document<br>extortion</span></div>
    <p class="method-text">Threat actors expose any sensitive document, file or written correspondence that would be embarrassing to the executive if publicly exposed. The most common extortion materials are legal documents, tax records, medical files and personal photos.</p>
  </div>
  <div class="row-rule" style="top:547px;"></div>

  <div class="method" style="top:557px;">
    <div class="method-tag"><span class="method-number">5</span><span class="method-label">Family<br>members</span></div>
    <p class="method-text">An executive’s children and spouse are often less physically protected and less cyber-aware, which makes them an easier target for exploitation and extortion.</p>
  </div>

  <div class="brand-mark"><span class="brand-square"></span>VALDREN</div>

  <p class="confidential-notice">CONFIDENTIAL – FOR INTERNAL USE ONLY</p>
</div>
</body>
</html>
```